This book will apply the 12 Steps to gaming addiction, also known as video game addiction. The primary purpose of the book is to provide an effective solution for this new type of addiction. The solution is based on the rich and successful concepts of traditional twelve-step programs like RL.

The title on the cover will be "Nine Doors Past the Glowing Screen" and "by Martin Quorby". A subtitle can be used if it works in your design of "A Practical Path Beyond Compulsive Console Play". Cover will be for a 6" x 9" book approximately 110 pages in length.

Some back cover text including some review quotes and an author bio are in the attached Word doc. There is also an author photo attached for for the back cover.

Requirements
Must have
• For the cover design it could be stylized, or an image, a partial image, or whatever. I am open to suggestions. Think about what would be noticed by a person searching for help with moderating their video game use, or by the parents or loved ones of problem gamers. Something contemporary and eye catching.

```html
<!DOCTYPE html>
<html lang="en">
<head>
<meta charset="UTF-8">
<title>Nine Doors Past the Glowing Screen — Martin Quorby</title>
<link rel="stylesheet" href="https://fonts.googleapis.com/css2?family=Montserrat:wght@500;600;700;800;900&display=swap">
<style>
  :root {
    --page-bg: #f4f4f4;
    --cover-bg: #140f2b;
    --neon-green: #2cf27c;
    --rule-yellow: #ecec1c;
    --title-pink: #e01c7c;
    --ink-white: #ffffff;
  }
  * { box-sizing: border-box; margin: 0; padding: 0; }
  html, body {
    width: 1200px; height: 1200px; overflow: hidden;
    background: var(--page-bg);
    font-family: "Montserrat", sans-serif;
  }
  .book-cover {
    position: absolute;
    left: 234px; top: 50px;
    width: 733px; height: 1100px;
    background: var(--cover-bg);
    overflow: hidden;
    color: var(--ink-white);
    text-align: center;
  }
  .cover-photo {
    position: absolute;
    left: 0; right: 0; top: 560px; bottom: 0;
    background:
      radial-gradient(ellipse 28% 34% at 50% 48%, rgba(120, 70, 110, 0.95), rgba(120, 70, 110, 0) 100%),
      linear-gradient(90deg, #5a86d8 10%, #c9d2f0 28%, #b88ac8 46%, #e2566e 62%, #e23048 78%, #7a9ee0 92%);
    -webkit-mask-image:
      linear-gradient(180deg, transparent 0%, #000 12%, #000 62%, rgba(0,0,0,0.35) 100%),
      linear-gradient(90deg, transparent 6%, #000 14%, #000 86%, transparent 94%);
    -webkit-mask-composite: source-in;
    mask-image:
      linear-gradient(180deg, transparent 0%, #000 12%, #000 62%, rgba(0,0,0,0.35) 100%),
      linear-gradient(90deg, transparent 6%, #000 14%, #000 86%, transparent 94%);
    mask-composite: intersect;
    opacity: 0.9;
  }
  .neon-title {
    position: absolute;
    left: 0; top: 78px;
    width: 733px; height: 140px;
  }
  .neon-title text {
    font-family: "Montserrat", sans-serif;
    font-weight: 700;
    font-size: 106px;
  }
  .neon-title .neon-stroke {
    fill: none;
    stroke: var(--neon-green);
    stroke-width: 9;
    stroke-linejoin: round;
  }
  .neon-title .neon-core {
    fill: var(--cover-bg);
    stroke: none;
  }
  .title-rule {
    position: absolute;
    left: 74px; right: 74px; top: 245px;
    display: flex; align-items: center; gap: 10px;
  }
  .title-rule .rule-line {
    flex: 1; height: 5px; border-radius: 3px;
    box-shadow: 0 0 8px rgba(236, 236, 28, 0.55);
  }
  .title-rule .rule-line.left { background: linear-gradient(90deg, rgba(236,236,28,0.25), var(--rule-yellow) 20%); }
  .title-rule .rule-line.right { background: linear-gradient(270deg, rgba(236,236,28,0.25), var(--rule-yellow) 20%); }
  .title-rule .rule-label {
    font-weight: 500; font-size: 28px; letter-spacing: 1px;
    position: relative; top: 4px;
  }
  .title-main {
    position: absolute; left: 0; right: 0; top: 282px;
    font-weight: 800; font-size: 70px; line-height: 78px;
    color: var(--title-pink);
    letter-spacing: 0.5px;
  }
  .subtitle {
    position: absolute; left: 0; right: 0; top: 456px;
    font-weight: 500; font-size: 29px; line-height: 40px;
    letter-spacing: 1.5px;
    text-transform: uppercase;
  }
  .author-name {
    position: absolute; left: 0; right: 0; top: 1000px;
    font-weight: 900; font-size: 62px; letter-spacing: 3px;
    text-transform: uppercase;
  }
</style>
</head>
<body>
  <main class="book-cover">
    <div class="cover-photo" role="img" aria-label="Photo of a child seen from behind holding a game controller in front of a brightly glowing television screen"></div>

    <svg class="neon-title" viewBox="0 0 733 140" role="img" aria-label="Nine Doors">
      <defs>
        <filter id="neon-glow" x="-10%" y="-30%" width="120%" height="160%">
          <feGaussianBlur stdDeviation="5" result="blur"/>
          <feMerge>
            <feMergeNode in="blur"/>
            <feMergeNode in="blur"/>
            <feMergeNode in="SourceGraphic"/>
          </feMerge>
        </filter>
      </defs>
      <text class="neon-stroke" x="366.5" y="118" text-anchor="middle" textLength="580" lengthAdjust="spacingAndGlyphs" filter="url(#neon-glow)">NINE DOORS</text>
      <text class="neon-core" x="366.5" y="118" text-anchor="middle" textLength="580" lengthAdjust="spacingAndGlyphs">NINE DOORS</text>
    </svg>

    <div class="title-rule">
      <span class="rule-line left"></span>
      <span class="rule-label">PAST THE</span>
      <span class="rule-line right"></span>
    </div>

    <h1 class="title-main">GLOWING<br>SCREEN</h1>

    <p class="subtitle">A Practical Path Beyond<br>Compulsive Console Play</p>

    <p class="author-name">Martin Quorby</p>
  </main>
</body>
</html>
```